DL Cards to get buyers attention

I’m looking to have four double-sided DL flyers professionally prepared and made print-ready in high resolution.

I have uploaded the four existing designs, and I’m happy for them to be reviewed with a fresh set of eyes. While I’m generally happy with the direction, I’m very open to recommendations around layout, typography, imagery, colour balance, spacing and overall presentation if there are opportunities to create a stronger and more professional result.

The key objective is to develop a consistent and recognisable suite of marketing material that strengthens both Jen Callow brand awareness and my personal profile in the local real estate market. Each flyer should feel like part of the same campaign while still having its own clear message and purpose.

I want the finished designs to feel professional, confident, modern and premium, without becoming overly busy or losing the simplicity that makes a DL flyer easy to read. Strong headlines, clear messaging and an obvious call to action are important. The Jen Callow branding should be immediately recognisable, while my photograph, name and contact details should be incorporated naturally and consistently.

Please review the existing designs and suggest any changes that would improve their visual impact, readability and consistency. I’m also open to seeing an alternative design direction if you believe there is a better overall look.

The final artwork needs to be supplied professionally print-ready at DL size (210 mm × 99 mm), double-sided, high resolution, CMYK where appropriate, with 3 mm bleed and safe margins, so it can be provided directly to a commercial printer.

The overall goal is simple: strong branding, professional presentation, consistent recognition and marketing material that people will remember.

Target Market(s)

People looking at selling their homes

Industry/Entity Type

Real Estate

Font styles to use
Serif
Sans Serif

Requirements
Must have
• Strong brand awareness - Jen Callow
Nice to have
• bright and fresh

```html
<!DOCTYPE html>
<html lang="en">
<head>
<meta charset="utf-8">
<title>Steps of a Sale – DL Flyer</title>
<link href="https://fonts.googleapis.com/css2?family=Archivo+Narrow:wght@700&family=Oswald:wght@200;300;600&family=Poppins:wght@500;600&family=Roboto+Condensed:wght@400;600;700&family=Roboto:wght@400;500;700&family=Cormorant+Garamond:ital,wght@0,500;1,500&display=swap" rel="stylesheet">
<style>
  :root {
    --brand-yellow: #ffe52b;
    --gold: #b59a12;
    --ink: #111111;
    --text: #222222;
    --paper: #ffffff;
    --backdrop: #808080;
    --rule: #c9c9c9;
  }
  * { box-sizing: border-box; margin: 0; padding: 0; }
  html, body { width: 1075px; height: 1200px; overflow: hidden; }
  body { background: var(--backdrop); position: relative; font-family: "Roboto", sans-serif; color: var(--text); }

  .card { position: absolute; left: 90px; width: 896px; height: 435px; overflow: hidden; }
  .card--front { top: 136px; }
  .card--back { top: 629px; background: var(--paper); }

  /* FRONT */
  .hero-photo {
    position: absolute; inset: 0;
    background:
      linear-gradient(90deg, rgba(10,20,25,.85) 0%, rgba(10,20,25,.55) 38%, rgba(10,20,25,0) 60%),
      linear-gradient(180deg, #a9c6d6 0%, #5e8a5a 28%, #d9cfb3 52%, #e6dcc2 66%, #5f7a3d 88%, #3f5a2a 100%);
  }
  .brand {
    position: absolute; right: 48px; top: 40px;
    display: flex; align-items: center; gap: 8px;
  }
  .brand__mark { width: 12px; height: 12px; background: var(--brand-yellow); }
  .brand__name { font-family: "Poppins", sans-serif; font-weight: 600; font-size: 17px; color: var(--paper); }

  .headline { position: absolute; inset: 0; }
  .headline span { position: absolute; left: 43px; line-height: 1; white-space: nowrap; }
  .headline__steps { top: 26px; font-family: "Archivo Narrow", sans-serif; font-weight: 700; font-size: 130px; letter-spacing: -2px; color: var(--paper); }
  .headline__ofa { top: 138px; left: 46px !important; font-family: "Oswald", sans-serif; font-weight: 200; font-size: 60px; color: var(--paper); }
  .headline__sale { top: 193px; font-family: "Archivo Narrow", sans-serif; font-weight: 700; font-size: 130px; letter-spacing: -2px; color: var(--brand-yellow); }
  .tagline {
    position: absolute; left: 45px; top: 330px;
    border-left: 2px solid var(--brand-yellow); padding-left: 15px;
    font-family: "Poppins", sans-serif; font-weight: 600; font-size: 15.5px; line-height: 20px; color: var(--paper);
  }

  /* BACK */
  .yellow-strip { position: absolute; left: 778px; top: 0; width: 118px; height: 100%; background: var(--brand-yellow); }
  .bottom-bar { position: absolute; left: 0; bottom: 0; width: 100%; height: 11px; background: var(--ink); z-index: 2; }
  .agent-photo { position: absolute; inset: 0; pointer-events: none; }
  .agent-photo__head {
    position: absolute; left: 714px; top: 73px; width: 118px; height: 150px;
    background: linear-gradient(180deg, #8a6a52 0%, #d2ab8e 30%, #c9997a 100%);
    border-radius: 55px 55px 50px 50px;
  }
  .agent-photo__shirt {
    position: absolute; left: 652px; top: 200px; width: 244px; height: 235px;
    background: linear-gradient(180deg, #f4f4f4 0%, #e6e6e6 100%);
    border-radius: 70px 0 0 0;
  }

  .steps { position: absolute; left: 44px; top: 48px; display: flex; gap: 12px; }
  .step { width: 116px; display: flex; flex-direction: column; }
  .step__head { display: flex; align-items: center; gap: 8px; height: 26px; }
  .step__num {
    width: 25px; height: 25px; border-radius: 50%; flex: none;
    background: var(--gold); border: 2px solid var(--brand-yellow);
    color: var(--paper); font-family: "Oswald", sans-serif; font-weight: 300; font-size: 11px;
    display: flex; align-items: center; justify-content: center;
  }
  .step__title { font-family: "Oswald", sans-serif; font-weight: 600; font-size: 9px; line-height: 9.5px; color: var(--ink); text-transform: uppercase; }
  .step__body {
    height: 253px; border: 1px solid var(--rule); border-top: none; border-radius: 0 0 10px 10px;
    padding: 10px 6px 0 10px; margin-top: -2px;
  }
  .item { margin-bottom: 7px; }
  .item__label {
    font-family: "Roboto", sans-serif; font-weight: 700; font-size: 8.5px; line-height: 10px; color: var(--ink);
    position: relative; padding-left: 11px;
  }
  .item__label::before {
    content: ""; position: absolute; left: 0; top: 2px; width: 6px; height: 6px; border-radius: 50%; background: var(--gold);
  }
  .item__label--plain::before { display: none; }
  .item__text { font-family: "Roboto Condensed", sans-serif; font-size: 6.6px; line-height: 10px; padding-left: 11px; margin-top: 3px; color: var(--text); }
  .tip { height: 68px; background: var(--brand-yellow); border-radius: 0 0 12px 12px; padding: 8px 10px; }
  .tip__label { font-family: "Roboto Condensed", sans-serif; font-weight: 700; font-size: 8.5px; color: #4a3f00; }
  .tip__text { font-family: "Roboto Condensed", sans-serif; font-size: 5.6px; line-height: 9px; color: #4a3f00; margin-top: 5px; }

  .contact { position: absolute; left: 563px; top: 42px; width: 148px; z-index: 1; }
  .contact__intro { font-family: "Cormorant Garamond", serif; font-style: italic; font-size: 15px; line-height: 20px; color: var(--ink); white-space: nowrap; }
  .contact__rule { width: 152px; height: 1px; background: #9a9a9a; margin: 14px 0 12px; }
  .contact__reach { font-family: "Roboto", sans-serif; font-size: 15px; color: var(--ink); }
  .contact__call { font-family: "Cormorant Garamond", serif; font-size: 17px; color: var(--ink); margin-top: 8px; }
  .contact__name { font-family: "Roboto", sans-serif; font-weight: 700; font-size: 27px; color: var(--ink); line-height: 28px; }
  .contact__phone {
    display: inline-flex; align-items: center; gap: 6px; margin-top: 8px;
    background: var(--ink); color: var(--paper); border-radius: 13px; height: 25px; padding: 0 12px 0 10px;
    font-family: "Roboto Condensed", sans-serif; font-weight: 700; font-size: 16px; white-space: nowrap;
  }
  .perks { list-style: none; margin-top: 10px; }
  .perks li {
    position: relative; padding-left: 16px; margin-bottom: 6px;
    font-family: "Roboto", sans-serif; font-size: 12.5px; line-height: 13px; color: var(--ink); width: 86px;
  }
  .perks svg { position: absolute; left: 0; top: 1px; }
</style>
</head>
<body>

<section class="card card--front">
  <div class="hero-photo" role="img" aria-label="Photo of a sunny coastal beach with hillside homes and a timber boardwalk"></div>
  <div class="brand"><span class="brand__mark"></span><span class="brand__name">Jen Callow</span></div>
  <h1 class="headline">
    <span class="headline__steps">STEPS</span>
    <span class="headline__ofa">OF A</span>
    <span class="headline__sale">SALE</span>
  </h1>
  <p class="tagline">A clear process. Proven results.<br>From listing to settlement, I'm<br>with you every step of the way.</p>
</section>

<section class="card card--back">
  <div class="yellow-strip"></div>
  <div class="agent-photo" role="img" aria-label="Portrait photo of the agent in a white branded shirt">
    <div class="agent-photo__head"></div>
    <div class="agent-photo__shirt"></div>
  </div>

  <div class="steps">
    <article class="step">
      <header class="step__head"><span class="step__num">01</span><h2 class="step__title">Preparation<br>&amp; Appraisal</h2></header>
      <div class="step__body">
        <div class="item"><p class="item__label">Agent selection</p><p class="item__text">Choose a local agent and set a realistic selling price based on market research.</p></div>
        <div class="item"><p class="item__label">Home styling</p><p class="item__text">Clean, declutter, and repair flaws to make the property photogenic. You can read Seven important tips for a successful sale from Jen Callow for guidance on staging your home.</p></div>
        <div class="item"><p class="item__label item__label--plain">Contract preparation</p><p class="item__text">Work with a solicitor or conveyancer to prepare the contract of sale &amp; vendor statement.</p></div>
      </div>
      <div class="tip"><p class="tip__label">JEN CALLOW TIP</p><p class="tip__text">Good preparation can make a big difference to how buyers see your property.</p></div>
    </article>

    <article class="step">
      <header class="step__head"><span class="step__num">02</span><h2 class="step__title">Choosing a<br>Method of Sale</h2></header>
      <div class="step__body">
        <div class="item"><p class="item__label">Auction</p><p class="item__text">Set a date, market without a price to build urgency, and encourage competitive bidding.</p></div>
        <div class="item"><p class="item__label">Private Treaty</p><p class="item__text">List an asking price and negotiate individual offers with buyers.</p></div>
        <div class="item"><p class="item__label">Expressions of Interest/ Tender</p><p class="item__text">Invite confidential offers by a set date for unique properties.</p></div>
      </div>
      <div class="tip"><p class="tip__label">JEN CALLOW TIP</p><p class="tip__text">The right method of sale depends on your property, the local market and your goals. Your agent can recommend the strategy best suited to achieving a</p></div>
    </article>

    <article class="step">
      <header class="step__head"><span class="step__num">03</span><h2 class="step__title">Preparation<br>&amp; Appraisal</h2></header>
      <div class="step__body">
        <div class="item"><p class="item__label">Launch your campaign</p><p class="item__text">Present your property to the market with professional photography, online advertising, signage and targeted promotion.</p></div>
        <div class="item"><p class="item__label">Inspections</p><p class="item__text">Hold open homes and private viewings to give prospective buyers the opportunity to experience your property.</p></div>
        <div class="item"><p class="item__label">Vendor reports</p><p class="item__text">Receive regular updates from your agent covering buyer feedback, inspection numbers, enquiry levels and overall market interest</p></div>
      </div>
      <div class="tip"><p class="tip__label">JEN CALLOW TIP</p><p class="tip__text">A strong marketing campaign creates exposure, builds buyer interest and helps generate competition for your property.</p></div>
    </article>

    <article class="step">
      <header class="step__head"><span class="step__num">04</span><h2 class="step__title">Contract<br>Exchange<br>&amp; Settlement</h2></header>
      <div class="step__body">
        <div class="item"><p class="item__label">Exchange</p><p class="item__text">Both buyer and seller sign separate copies of the contract, and they are swapped.</p></div>
        <div class="item"><p class="item__label">Deposit</p><p class="item__text">The buyer pays a deposit (usually 10%), which is held in a trust account.</p></div>
        <div class="item"><p class="item__label">Cooling-off</p><p class="item__text">Private treaty sales usually include a 5-day cooling-off period for buyers (none at auction).</p></div>
        <div class="item"><p class="item__label">Settlement</p><p class="item__text">The final transaction is completed, typically 42 days (six weeks) after exchange, and keys are handed over.</p></div>
      </div>
      <div class="tip"><p class="tip__label">JEN CALLOW TIP</p><p class="tip__text">Your agent, solicitor or conveyancer will guide you through the final steps from exchange through to settlement and key handover.</p></div>
    </article>
  </div>

  <div class="contact">
    <p class="contact__intro">If you are<br>thinking of selling<br>planning to sell or<br>would simply like to<br>chat about your options..</p>
    <div class="contact__rule"></div>
    <p class="contact__reach">Reach out and</p>
    <p class="contact__call">Call me today.</p>
    <p class="contact__name">Mark</p>
    <p class="contact__phone">
      <svg width="14" height="14" viewBox="0 0 24 24" aria-hidden="true"><path fill="#ffe52b" d="M6.6 10.8a15.1 15.1 0 0 0 6.6 6.6l2.2-2.2a1 1 0 0 1 1-.25 11.4 11.4 0 0 0 3.6.57 1 1 0 0 1 1 1V20a1 1 0 0 1-1 1A17 17 0 0 1 3 4a1 1 0 0 1 1-1h3.5a1 1 0 0 1 1 1c0 1.25.2 2.45.57 3.57a1 1 0 0 1-.25 1z"/></svg>
      0400 123 456
    </p>
    <ul class="perks">
      <li><svg width="11" height="11" viewBox="0 0 12 12" aria-hidden="true"><circle cx="6" cy="6" r="6" fill="#b59a12"/><path d="M3.3 6.2l1.8 1.8 3.6-3.8" stroke="#fff" stroke-width="1.4" fill="none"/></svg>Local Knowledge</li>
      <li><svg width="11" height="11" viewBox="0 0 12 12" aria-hidden="true"><circle cx="6" cy="6" r="6" fill="#b59a12"/><path d="M3.3 6.2l1.8 1.8 3.6-3.8" stroke="#fff" stroke-width="1.4" fill="none"/></svg>Exceptional Service</li>
      <li><svg width="11" height="11" viewBox="0 0 12 12" aria-hidden="true"><circle cx="6" cy="6" r="6" fill="#b59a12"/><path d="M3.3 6.2l1.8 1.8 3.6-3.8" stroke="#fff" stroke-width="1.4" fill="none"/></svg>Genuine Care</li>
    </ul>
  </div>

  <div class="bottom-bar"></div>
</section>

</body>
</html>
```